New young doctors office business card

Doctor's office
Hello:
My name is Dr. Marcos Teodoro Beltrán Oquendo. I need a business card for my new office located within a hospital. The name of the hospital is "Hospital Almendral". Although the hospital logo and name must be included in the business card, please make me a personal logo for myself. The logo might be maybe my name in a stylish font, or my initials (MTBO) or something like that. Im more inclined to a font logo, rather than a image logo, but a good one might change my mind. The info on my business card is going to be in spanish. The following info must be included please (the info within parenthesis is not to be included, it is provided for you to understand it since it's in spanish, so you can properly place it on the card):
-Dr. Marcos Teodoro Beltrán Oquendo (my name)
-Medicina general (My specialty)
-Hospital Almendral (The name of the hospital where my office is)
-Calle Pedro Ibarra #374 Col. Almendral (address)
-Tel 417-5860 (Office phone)
-Sábado y domingo 10:00 am a 10:00pm (Office hours)
-Emergencias: 593-761-4028 (Emergency phone)
-teodorobo@mensavia.com (email)
-English Spoken
So, that's all the info i need to be on the business card. Although it's a business card for a doctor's office, i dont want it to be a boring, plain business card. Make it eye-catchy and stylish please. As i said, the hospital logo must be included. You'll find it on the heading of the PDF file i attached, but dont make it the center of attention.
Industry/Entity Type
Physician
Contact Information for Business Card
Hello:My name is Dr. Marcos Teodoro Beltrán Oquendo. I need a business card for my new office located within a hospital. The name of the hospital is "Hospital Almendral". Although the hospital logo and name must be included in the business card, please make me a personal logo for myself. The logo might be maybe my name in a stylish font, or my initials (MTBO) or something like that. Im more inclined to a font logo, rather than a image logo, but a good one might change my mind. The info on my business card is going to be in spanish. The following info must be included please (the info within parenthesis is not to be included, it is provided for you to understand it since it's in spanish, so you can properly place it on the card):-Dr. Marcos Teodoro Beltrán Oquendo (my name)-Medicina general (My specialty)-Hospital Almendral (The name of the hospital where my office is)-Calle Pedro Ibarra #374 Col. Almendral (address)-Tel 417-5860 (Office phone)-Sábado y domingo 10:00 am a 10:00pm (Office hours)-Emergencias: 593-761-4028 (Emergency phone)-teodorobo@mensavia.com (email)-English Spoken So, that's all the info i need to be on the business card. Although it's a business card for a doctor's office, i dont want it to be a boring, plain business card. Make it eye-catchy and stylish please. As i said, the hospital logo must be included. You'll find it on the heading of the PDF file i attached, but dont make it the center of attention.
Look and feel
Each slider illustrates characteristics of the customer's brand and the style your logo design should communicate.

```html
<!DOCTYPE html>
<html lang="es">
<head>
<meta charset="utf-8">
<title>Dr. MTBO – Tarjeta de presentación</title>
<link rel="stylesheet" href="https://fonts.googleapis.com/css2?family=Cabin:wght@400;600;700&display=swap">
<style>
  :root {
    --stage: #2a2f36;
    --blue-light: #559ee2;
    --blue-mid: #3b78cc;
    --blue-deep: #2146a0;
    --slate-light: #3f4d5f;
    --slate-dark: #1d242e;
    --paper: #ffffff;
    --ink-light: #f2f5f8;
    --accent-cyan: #86e4f2;
    --logo-blue: #2a5cb8;
  }
  * { margin: 0; padding: 0; box-sizing: border-box; }
  html, body {
    width: 1200px; height: 1200px; overflow: hidden;
    background: var(--stage);
    font-family: "Cabin", sans-serif;
  }
  .canvas {
    width: 1200px; height: 1200px;
    display: flex; flex-direction: column; align-items: center; justify-content: center;
    gap: 60px;
  }
  .card {
    position: relative;
    width: 900px; height: 500px;
    overflow: hidden;
    box-shadow: 0 12px 30px rgba(0,0,0,.35);
  }

  /* Front */
  .card-front {
    background: linear-gradient(100deg, var(--blue-light) 0%, var(--blue-mid) 45%, var(--blue-deep) 100%);
  }
  .personal-mark {
    position: absolute; left: 50%; top: 44%;
    transform: translate(-50%, -50%);
    color: var(--ink-light);
    font-weight: 700;
    line-height: 1;
  }
  .personal-mark .title { display: block; font-size: 34px; margin-bottom: 4px; }
  .personal-mark .initials { display: block; font-size: 110px; letter-spacing: 2px; }
  .hospital-tab {
    position: absolute; left: 50%; bottom: 0;
    transform: translateX(-50%);
    width: 150px; height: 82px;
    background: var(--paper);
    display: flex; align-items: center; justify-content: center;
    color: var(--logo-blue);
    font-weight: 700; font-size: 20px;
  }

  /* Back */
  .card-back { display: flex; }
  .edge-band {
    width: 42px;
    background: linear-gradient(180deg, var(--blue-light), var(--blue-deep));
  }
  .logo-panel {
    width: 330px; background: var(--paper);
    display: flex; align-items: center; justify-content: center;
  }
  .logo-panel .personal-mark {
    position: static; transform: none; color: var(--logo-blue);
  }
  .logo-panel .title { font-size: 22px; }
  .logo-panel .initials { font-size: 72px; }
  .info-panel {
    flex: 1;
    background: linear-gradient(110deg, var(--slate-light) 0%, var(--slate-dark) 100%);
    color: var(--ink-light);
    text-align: right;
    padding: 40px 30px 0 20px;
    font-size: 21px;
    line-height: 1.3;
  }
  .info-group { margin-bottom: 22px; }
  .doctor-name { font-size: 22px; }
  .specialty { color: var(--accent-cyan); font-weight: 700; font-size: 23px; }
</style>
</head>
<body>
<main class="canvas">
  <section class="card card-front" aria-label="Frente de la tarjeta">
    <div class="personal-mark">
      <span class="title">Dr.</span>
      <span class="initials">MTBO</span>
    </div>
    <div class="hospital-tab">Almendral</div>
  </section>

  <section class="card card-back" aria-label="Reverso de la tarjeta">
    <div class="edge-band"></div>
    <div class="logo-panel">
      <div class="personal-mark">
        <span class="title">Dr.</span>
        <span class="initials">MTBO</span>
      </div>
    </div>
    <div class="info-panel">
      <div class="info-group">
        <p class="doctor-name">Dr. Marcos Teodoro Beltrán Oquendo</p>
        <p class="specialty">Medicina general</p>
      </div>
      <div class="info-group">
        <p>Hospital Almendral</p>
        <p>Calle Pedro Ibarra #374 Col. Almendral</p>
      </div>
      <div class="info-group">
        <p>Tel: 417-5860</p>
        <p>Sábado y domingo 10:00 am a 10:00pm</p>
        <p>Emergencias: 593-761-4028</p>
        <p>teodorobo@mensavia.com</p>
      </div>
      <p>English Spoken</p>
    </div>
    <div class="edge-band"></div>
  </section>
</main>
</body>
</html>
```